Newsletter-Design für Motorradunternehmen
Zielgruppe
Wir sind in der Motorradbranche tätig.
Unser Producktportfoglio erstreckt sich von Motorräder über Motorradbekleidung, bis hinzu Events und spezielle Umbauten.
Unsere Zielgruppe ist sehr breit .
Alter: 16-70 Jahre
Da wir Premium-Produkte verkaufen erwarten unsere Kunden gute Qualität.
Aufgabenstellung
Wir wollen ein neuen Newsletter Designen, dieser soll frisch und modern wirken.
Besonders grossen Wert legen wir auf den Header des Newsletters.
Zudem sollte der Header leicht auf eine andere Marke umwandelbar sein, für die verschiedenen Marken müssen wir zum Teil auch anderen Header verwenden (zum Beispiel nur ein eigenen Newsletter für alle KVL Kunden).
Wir arbeiten mit Postfach4ME, dieses Programm bietet verschiedene Bausteine an, wie Bild, Text usw. (Ein Bild der Bausteine ist in den Downloads zu sehen.)
Wir sind gespannt, was euch so einfällt.

```html
<!DOCTYPE html>
<html lang="de">
<head>
<meta charset="utf-8">
<title>Moto Kessler Newsletter</title>
<link rel="stylesheet" href="https://fonts.googleapis.com/css2?family=Noto+Sans:wght@400;700&family=Lato:wght@400;700&family=Oswald:wght@600&display=swap">
<style>
:root{
  --bg:#000;
  --text:#fff;
  --brand-red:#e30613;
  --sale-red:#e8321c;
  --footer-bg:#7b7b7b;
  --footer-text:#f2f2f2;
  --sun-core:#fff6c8;
  --sun-glow:#ffc93a;
  --sky-orange:#f07a16;
  --sky-deep:#c9400f;
  --ground:#1a0803;
  --forest:#3f4a1e;
  --forest-dark:#2b3314;
  --sky-blue:#7d8fa6;
  --road:#8c8f90;
}
*{margin:0;padding:0;box-sizing:border-box}
html,body{width:1200px;height:2856px;overflow:hidden;background:var(--bg)}
body{position:relative;color:var(--text);font-family:"Noto Sans",Verdana,sans-serif}

/* Header */
.hero{position:absolute;left:0;top:0;width:1200px;height:360px;overflow:hidden;
  background:
    radial-gradient(circle at 470px 62px,var(--sun-core) 0,var(--sun-glow) 34px,rgba(255,160,30,.85) 90px,rgba(240,110,20,0) 300px),
    radial-gradient(ellipse 900px 260px at 470px 120px,rgba(255,120,20,.9) 0,rgba(230,90,15,.6) 55%,rgba(120,30,5,0) 100%),
    linear-gradient(180deg,#7a2a0c 0,var(--sky-deep) 18%,var(--sky-orange) 45%,#b8420e 62%,var(--ground) 76%,var(--bg) 100%)}
.hero-ground{position:absolute;left:0;bottom:0;width:1200px;height:130px}
.hero-figure{position:absolute;left:300px;top:20px;width:420px;height:250px;
  background:radial-gradient(ellipse at 50% 60%,rgba(20,6,2,.85) 0,rgba(20,6,2,.5) 45%,rgba(20,6,2,0) 72%)}
.brand{position:absolute;right:64px;top:40px;display:flex;align-items:center;gap:14px}
.brand-mark{width:30px;height:30px;background:var(--brand-red)}
.brand-name{font-weight:700;font-size:36px;color:var(--text);letter-spacing:1px}

/* Intro */
.headline{position:absolute;left:66px;top:504px;font-size:35px;font-weight:700;letter-spacing:1.5px}
.intro{position:absolute;left:66px;top:648px;width:1080px;font-size:24px;line-height:29px;letter-spacing:.8px}
.intro p{margin-bottom:29px}
.intro .sender{margin-top:44px}
.signature{position:absolute;left:66px;top:938px;width:196px;height:98px;
  background:radial-gradient(ellipse at 50% 55%,#262626 0,#111 60%,#000 100%)}
.section-title{position:absolute;left:66px;top:1124px;font-size:24px;font-weight:700;letter-spacing:1.5px}

/* Offers */
.offer{position:absolute;left:66px;width:1080px;height:340px}
.offer-visual{position:absolute;left:0;top:0;width:540px;height:334px;overflow:hidden;
  background:
    radial-gradient(ellipse 170px 110px at 400px 220px,rgba(30,30,30,.75) 0,rgba(200,90,30,.35) 55%,rgba(0,0,0,0) 100%),
    linear-gradient(180deg,var(--sky-blue) 0,#6a7560 9%,var(--forest) 22%,var(--forest-dark) 55%,#4d5530 72%,var(--road) 86%,#6f7375 100%)}
.sale{position:absolute;left:6px;top:12px;font-family:Oswald,"Arial Narrow",sans-serif;font-weight:600;
  color:var(--sale-red);text-transform:uppercase;line-height:68px}
.sale-main{font-size:66px;letter-spacing:3px;line-height:76px}
.sale-sub{font-size:46px;letter-spacing:1px}
.offer-body{position:absolute;left:582px;top:0;width:500px}
.offer-title{font-size:24px;font-weight:700;letter-spacing:1.5px;margin-bottom:10px}
.offer-text{font-size:24px;line-height:29px;letter-spacing:.8px}
.offer-link{display:block;margin-top:24px;font-size:24px;color:var(--text);text-decoration:none;letter-spacing:.8px}

/* Footer */
.footer{position:absolute;left:0;top:2490px;width:1200px;height:366px;background:var(--footer-bg);
  font-family:Lato,Arial,sans-serif;color:var(--footer-text);font-size:17px;line-height:26px}
.footer-cell{position:absolute;width:270px}
.footer h3{font-size:18px;font-weight:700;line-height:22px;color:#fff;margin-bottom:10px}
.social{display:flex;gap:14px;margin-top:18px}
.social-item{display:flex;align-items:center;gap:8px;font-size:15px}
.social-square{width:36px;height:36px;background:#d6d6d6;border-radius:6px}
.mail{display:flex;align-items:center;gap:10px}
</style>
</head>
<body>
<header class="hero" role="img" aria-label="Silhouette einer Motorradfahrerin neben ihrem Motorrad vor orangem Sonnenuntergang über einer Wiese">
  <div class="hero-figure"></div>
  <svg class="hero-ground" viewBox="0 0 1200 130" preserveAspectRatio="none" aria-hidden="true">
    <defs><linearGradient id="groundFade" x1="0" y1="0" x2="0" y2="1"><stop offset="0" stop-color="#1a0803"/><stop offset="1" stop-color="#000"/></linearGradient></defs>
    <path d="M0 38 C150 30 260 44 400 36 S700 26 860 38 S1100 44 1200 32 L1200 130 L0 130 Z" fill="url(#groundFade)"/>
  </svg>
  <div class="brand"><span class="brand-mark"></span><span class="brand-name">MOTO KESSLER</span></div>
</header>

<h1 class="headline">NEWSLETTERHEADLINE</h1>

<div class="intro">
  <p>Hallo Max Mustermann,</p>
  <p>auch diesen Monat haben wir wieder speziell für Sie ausgewählte Angebote.<br>Für Sie nur das beste, zum Vorteilspreis für Newsletterkunden. Benutzen Sie den<br>Aktionscode “FLOWRIDER” und sichern Sie sich an der Kasse 10 % auf Ihren<br>nächsten Einkauf.</p>
  <p class="sender">Max Mustermann</p>
</div>
<div class="signature" role="img" aria-label="Handschriftliche Unterschrift"></div>

<h2 class="section-title">UNSERE ANGEBOTE FÜR SIE</h2>

<section class="offer" style="top:1216px">
  <div class="offer-visual" role="img" aria-label="Aktionsbild: Motorradfahrer in Kurvenlage vor Waldkulisse">
    <div class="sale"><div class="sale-main">Summer Sale</div><div class="sale-sub">Bis zu<br>CHF 3490.-<br>Sparen</div></div>
  </div>
  <div class="offer-body">
    <h3 class="offer-title">ANGEBOT 1</h3>
    <p class="offer-text">Lorem ipsum dolor sit amet, consetetur sadipscing elitr, sed diam nonumy eirmod tempor invidunt ut labore et dolore magna aliquyam erat, sed diam voluptua. At vero eos et accusam et justo duo dolores et ea rebum. Stet clita kasd guberg no sea takimata sanctus est Lorem ipsum dolor.</p>
    <a class="offer-link" href="#">› Zum Angebot</a>
  </div>
</section>

<section class="offer" style="top:1618px">
  <div class="offer-visual" role="img" aria-label="Aktionsbild: Motorradfahrer in Kurvenlage vor Waldkulisse">
    <div class="sale"><div class="sale-main">Summer Sale</div><div class="sale-sub">Bis zu<br>CHF 3490.-<br>Sparen</div></div>
  </div>
  <div class="offer-body">
    <h3 class="offer-title">ANGEBOT 2</h3>
    <p class="offer-text">Lorem ipsum dolor sit amet, consetetur sadipscing elitr, sed diam nonumy eirmod tempor invidunt ut labore et dolore magna aliquyam erat, sed diam voluptua. At vero eos et accusam et justo duo dolores et ea rebum. Stet clita kasd guberg no sea takimata sanctus est Lorem ipsum dolor.</p>
    <a class="offer-link" href="#">› Zum Angebot</a>
  </div>
</section>

<section class="offer" style="top:2036px">
  <div class="offer-visual" role="img" aria-label="Aktionsbild: Motorradfahrer in Kurvenlage vor Waldkulisse">
    <div class="sale"><div class="sale-main">Summer Sale</div><div class="sale-sub">Bis zu<br>CHF 3490.-<br>Sparen</div></div>
  </div>
  <div class="offer-body">
    <h3 class="offer-title">ANGEBOT 3</h3>
    <p class="offer-text">Lorem ipsum dolor sit amet, consetetur sadipscing elitr, sed diam nonumy eirmod tempor invidunt ut labore et dolore magna aliquyam erat, sed diam voluptua. At vero eos et accusam et justo duo dolores et ea rebum. Stet clita kasd guberg no sea takimata sanctus est Lorem ipsum dolor.</p>
    <a class="offer-link" href="#">› Zum Angebot</a>
  </div>
</section>

<footer class="footer">
  <div class="footer-cell" style="left:54px;top:34px">
    <h3>Besuche uns in den sozialen<br>Medien</h3>
    <div class="social">
      <span class="social-item"><span class="social-square"></span>Rideboard</span>
      <span class="social-item"><span class="social-square"></span>Clipkanal</span>
    </div>
  </div>
  <div class="footer-cell" style="left:340px;top:34px">
    <h3>Unser Kundendienst unter-<br>stützt Dich:</h3>
    <p>Wir sind auch bei einem<br>Notfall für Dich da:<br>+41 00 000 12 34</p>
  </div>
  <div class="footer-cell" style="left:628px;top:34px">
    <h3>So findest Du uns:</h3>
    <p>Moto Kessler AG<br>Birkenweg 12<br>5400 Mühlental</p>
  </div>
  <div class="footer-cell" style="left:914px;top:34px">
    <h3>Dialog mit uns:</h3>
    <p class="mail">
      <svg width="22" height="16" viewBox="0 0 22 16" aria-hidden="true"><rect x="1" y="1" width="20" height="14" fill="none" stroke="#f2f2f2" stroke-width="2"/><path d="M1 1 L11 9 L21 1" fill="none" stroke="#f2f2f2" stroke-width="2"/></svg>
      info@moto-kessler.ch
    </p>
  </div>
  <div class="footer-cell" style="left:340px;top:190px">
    <h3>Öffnungszeiten</h3>
    <p>Dienstag bis Freitag<br>08.00 - 12.00 Uhr<br>13.30 - 18.30 Uhr</p>
  </div>
  <div class="footer-cell" style="left:628px;top:190px">
    <p>Ab sofort bis Ende Oktober<br>Donnerstags Abendverkauf<br>08.00 - 12.00 Uhr<br>13.30 - 20.00 Uhr</p>
  </div>
  <div class="footer-cell" style="left:914px;top:190px">
    <p>Samstag<br>08.00 - 16.00 Uhr<br>März - Oktober Töfftreffen mit<br>Grillplausch</p>
  </div>
</footer>
</body>
</html>
```